Postcard Design to introduce Plinkett Drip Solutions services

Company name: Indoor Water ConservationCustom fitted products for sinks, showers and toilets.Average savings 20%ROI 6 to 12 monthsNote: we just joined this organization and want to use this postcard to "introduce" our Company and services so that when they think of conserving water indoors, they think of use. In your images section are our logo (we have other resolutions if needed) and an image - we are open to suggestions for design and what to include.One suggestion is to introduce us and use the New Years Resolution - even if conserving water and saving money are not our new year's resolution, when you are ready to conserve water and save money, think of us.

Target Market(s)

2 markets - 1) hotels and 2) apartment complexes. 2 markets, 2 postcards, 2 mailing lists

Industry/Entity Type

It Company

Colors
85acd3
33a6d7
33b8a4

Requirements
Must have
• logo, company name, ave savings 20%, ROI 6 - 12 months, introduction that we are new service provider to 1) Marrowby Innkeepers and Hospitality Association (1 mailing/1 postcard) and new service provider to 2) Tellaview Rental Housing Association (2nd mailing/2nd postcard).
Nice to have
• Using the concept of New Year's resolution, maybe a finger with a string tied to it about to turn off a faucet - or some similar image.

```html
<!DOCTYPE html>
<html lang="en">
<head>
<meta charset="utf-8">
<title>Plinkett Drip Solutions – Postcard</title>
<link rel="stylesheet" href="https://fonts.googleapis.com/css2?family=Oswald:wght@300;500;600&family=Lato:wght@400;700;900&display=swap">
<style>
  :root{
    --backdrop:#ebe7e2;
    --white:#ffffff;
    --blue:#1f6fbf;
    --sky:#33a6d7;
    --pale:#85acd3;
    --teal:#33b8a4;
    --charcoal:#454545;
    --ink:#2b2b2b;
    --black:#111111;
    --stamp:#d4d6d8;
  }
  *{box-sizing:border-box;margin:0;padding:0}
  html,body{width:907px;height:1200px;overflow:hidden}
  body{background:var(--backdrop);position:relative;font-family:"Lato",sans-serif;color:var(--ink)}
  .card{position:absolute;left:124px;width:659px;background:var(--white);overflow:hidden;box-shadow:0 2px 6px rgba(0,0,0,.18)}
  .card--front{top:80px;height:512px}
  .card--back{top:627px;height:511px;background:linear-gradient(180deg,#e6e7e8 0%,#ffffff 55%,#f2f2f2 100%)}
  .card svg.shapes{position:absolute;inset:0;width:100%;height:100%}
  .abs{position:absolute}

  /* front */
  .splash{left:0;top:0;width:300px;height:330px;background:radial-gradient(ellipse at 55% 45%,#bcd5ec 0%,#85acd3 38%,rgba(255,255,255,0) 70%)}
  .headline{right:22px;top:34px;text-align:right;font-family:"Oswald",sans-serif;line-height:1}
  .headline__main{display:block;font-size:45px;font-weight:600;color:var(--white);letter-spacing:.5px}
  .headline__sub{display:block;font-size:30px;font-weight:300;color:var(--black);letter-spacing:1.5px;margin-top:4px}
  .badge{left:195px;top:207px;width:132px;height:132px;border-radius:50%;text-align:center;color:var(--white);padding-top:26px}
  .badge__title{font-size:22px;font-weight:700;color:var(--teal);line-height:1.05}
  .badge__value{font-size:16px;font-weight:900;color:var(--teal);line-height:1.2}
  .badge__roi{font-size:15px;line-height:1.25}
  .pitch{right:22px;top:266px;text-align:right}
  .pitch__big{font-family:"Oswald",sans-serif;font-weight:600;font-size:52px;line-height:1;color:var(--blue)}
  .pitch__line{font-size:18px;font-weight:700;color:var(--ink);margin-top:6px}
  .pitch__small{font-size:14px;color:var(--ink);margin-top:1px}
  .brand{display:flex;align-items:center;gap:8px;font-weight:900;color:var(--sky);line-height:1.05}
  .brand__dot{border-radius:50%;background:var(--sky);flex:none}
  .card--front .brand{left:18px;top:384px;width:185px;font-size:20px}
  .card--front .brand__dot{width:34px;height:34px}
  .contact{text-align:right;color:var(--white)}
  .card--front .contact{right:22px;top:396px}
  .contact__label{font-size:20px;font-weight:700;color:var(--teal);margin-bottom:4px}
  .contact__row{display:flex;justify-content:flex-end;align-items:center;gap:6px;line-height:1.5}
  .contact__phone{font-size:18px;font-weight:900}
  .contact__text{font-size:13.5px}
  .icon{width:12px;height:12px;fill:var(--teal);flex:none}

  /* back */
  .card--back .brand{left:30px;top:56px;width:300px;font-size:30px}
  .card--back .brand__dot{width:56px;height:56px}
  .benefits-head{left:0;top:185px;width:345px;height:83px;background:var(--charcoal);padding:15px 0 0 32px;font-size:20px;font-weight:400;line-height:1.3;color:var(--white)}
  .benefits-head strong{color:var(--teal);font-weight:700}
  .benefits{left:34px;top:290px;width:275px;list-style:none;font-size:15.5px;font-weight:700;color:var(--ink)}
  .benefits li{position:relative;padding-left:22px;line-height:1.28;margin-bottom:3px}
  .benefits svg{position:absolute;left:0;top:3px;width:15px;height:13px;stroke:var(--teal);stroke-width:3;fill:none}
  .card--back .contact{top:447px;right:264px}
  .card--back .contact__phone{font-size:14px;font-weight:700}
  .card--back .contact__text{font-size:13px}
  .card--back .contact__row{line-height:1.4}
  .stamp{right:16px;top:15px;width:70px;height:78px;background:var(--stamp)}
</style>
</head>
<body>

<section class="card card--front">
  <svg class="shapes" viewBox="0 0 659 512" preserveAspectRatio="none" aria-hidden="true">
    <defs>
      <linearGradient id="blueBand" x1="0" y1="0" x2="1" y2="1">
        <stop offset="0" stop-color="#17529a"/>
        <stop offset=".6" stop-color="#1f6fbf"/>
        <stop offset="1" stop-color="#2f86d0"/>
      </linearGradient>
    </defs>
    <path d="M200 0H659V170C560 150 420 175 320 260H200Z" fill="url(#blueBand)"/>
    <path d="M320 260C420 175 560 150 659 170V192C560 172 430 195 330 272Z" fill="#33b8a4"/>
    <path d="M336 282C435 207 560 187 659 207V218C560 198 440 218 342 292Z" fill="#454545"/>
    <circle cx="110" cy="140" r="226" fill="none" stroke="#33b8a4" stroke-width="5"/>
    <circle cx="110" cy="140" r="215" fill="#ffffff" stroke="#454545" stroke-width="10"/>
    <path d="M212 356C238 390 244 450 236 512" fill="none" stroke="#454545" stroke-width="8"/>
    <path d="M226 352C252 388 258 450 250 512" fill="none" stroke="#33b8a4" stroke-width="4"/>
    <path d="M262 512C262 470 272 446 306 442H350C392 442 420 382 462 380H659" fill="none" stroke="#33b8a4" stroke-width="5"/>
    <path d="M276 512C276 475 286 456 314 454H356C398 454 426 392 468 392H659V512Z" fill="#454545"/>
    <circle cx="261" cy="273" r="68" fill="#111111" stroke="#33a6d7" stroke-width="4"/>
  </svg>
  <div class="abs splash" role="img" aria-label="Illustration of a bird formed from splashing water"></div>
  <svg class="abs" style="left:193px;top:205px;width:136px;height:136px" viewBox="0 0 136 136" aria-hidden="true"><circle cx="68" cy="68" r="66" fill="#111111" stroke="#33a6d7" stroke-width="4"/></svg>

  <h1 class="abs headline"><span class="headline__main">PLINKETT DRIP</span><span class="headline__sub">SOLUTIONS</span></h1>

  <div class="abs badge">
    <div class="badge__title">Savings</div>
    <div class="badge__value">over 20%</div>
    <div class="badge__roi">ROI 6 to 12<br>months</div>
  </div>

  <div class="abs pitch">
    <div class="pitch__big">DO MORE</div>
    <div class="pitch__line">than just low flow shower heads</div>
    <div class="pitch__small">aerators and low flow toilets to Save More</div>
  </div>

  <div class="abs brand"><span class="brand__dot"></span><span>Plinkett Drip Solutions</span></div>

  <div class="abs contact">
    <div class="contact__label">contact us</div>
    <div class="contact__row"><span class="contact__phone">(555) 014- 2290</span><svg class="icon" viewBox="0 0 12 12"><rect x="3" y="0" width="6" height="12" rx="1"/></svg></div>
    <div class="contact__row"><span class="contact__text">info@plinkettdrip.com</span><svg class="icon" viewBox="0 0 12 12"><path d="M0 2h12v8H0z"/></svg></div>
    <div class="contact__row"><span class="contact__text">www.plinkettdripsolutions.com</span><svg class="icon" viewBox="0 0 12 12"><circle cx="6" cy="6" r="5.5"/></svg></div>
  </div>
</section>

<section class="card card--back">
  <svg class="shapes" viewBox="0 0 659 511" preserveAspectRatio="none" aria-hidden="true">
    <path d="M0 430H298C348 430 372 410 410 384" fill="none" stroke="#33b8a4" stroke-width="4"/>
    <path d="M0 440H300C350 440 380 420 418 394L440 511H0Z" fill="#454545"/>
    <path d="M380 0C340 60 332 130 345 200C360 290 430 360 432 440C433 470 425 495 415 511H659V0Z" fill="#ffffff"/>
    <path d="M380 0C340 60 332 130 345 200C360 290 430 360 432 440C433 470 425 495 415 511" fill="none" stroke="#33a6d7" stroke-width="6"/>
    <path d="M405 0C366 60 358 130 370 200C385 290 452 360 454 440C455 470 447 495 437 511" fill="none" stroke="#33b8a4" stroke-width="3"/>
  </svg>

  <div class="abs stamp" aria-hidden="true"></div>

  <div class="abs brand"><span class="brand__dot"></span><span>Plinkett Drip Solutions</span></div>

  <h2 class="abs benefits-head"><strong>OUR SOLUTIONS PROVIDE</strong><br>THE FOLLOWING BENEFITS</h2>

  <ul class="abs benefits">
    <li><svg viewBox="0 0 15 13"><path d="M1 7l4 4 9-10"/></svg>Reduction of overall water consumption while maintaining “guest” satisfaction and utility</li>
    <li><svg viewBox="0 0 15 13"><path d="M1 7l4 4 9-10"/></svg>Reduced Water-Related Costs</li>
    <li><svg viewBox="0 0 15 13"><path d="M1 7l4 4 9-10"/></svg>Increased Profitability</li>
    <li><svg viewBox="0 0 15 13"><path d="M1 7l4 4 9-10"/></svg>Rebate and incentive administration</li>
  </ul>

  <div class="abs contact">
    <div class="contact__row"><span class="contact__phone">(555) 014- 2290</span><svg class="icon" viewBox="0 0 12 12"><rect x="3" y="0" width="6" height="12" rx="1"/></svg></div>
    <div class="contact__row"><span class="contact__text">info@plinkettdrip.com</span><svg class="icon" viewBox="0 0 12 12"><path d="M0 2h12v8H0z"/></svg></div>
    <div class="contact__row"><span class="contact__text">www.plinkettdripsolutions.com</span><svg class="icon" viewBox="0 0 12 12"><circle cx="6" cy="6" r="5.5"/></svg></div>
  </div>
</section>

</body>
</html>
```